Flyer Template

I need a flyer template for door knocking on properties. Text Boxes need to be editable, with a header and text body. Footer to be my info. Project to be stylized to match my real estate signs and logo art from past projects

```html
<!DOCTYPE html>
<html lang="en">
<head>
<meta charset="utf-8">
<title>Listing Flyer – 4820 N Birch Lane #B3</title>
<link href="https://fonts.googleapis.com/css2?family=Roboto+Condensed:wght@400;700&family=Montserrat:wght@400;600&display=swap" rel="stylesheet">
<style>
  :root{
    --red:#e31e24;
    --black:#0a0a0a;
    --paper:#f1f1f1;
    --white:#ffffff;
    --ink:#1b1b1b;
    --panel-grey:#9b9b9e;
    --panel-head:#ececec;
    --panel-body:#f7f7f7;
    --stage:#d9d9d9;
  }
  *{margin:0;padding:0;box-sizing:border-box}
  html,body{width:1200px;height:1200px;overflow:hidden;background:var(--stage)}
  body{font-family:"Roboto Condensed",Arial,sans-serif;color:var(--ink)}
  .flyer{position:absolute;left:189px;top:20px;width:822px;height:1160px;background:var(--paper);overflow:hidden}

  .hero-photo{position:absolute;left:0;top:0;width:822px;height:405px;
    background:linear-gradient(180deg,#e6e8ea 0%,#c9ccd0 35%,#9ea2a7 70%,#d8dadd 100%)}

  .thumb{position:absolute;top:357px;width:246px;height:176px;background:var(--white);padding:6px}
  .thumb div{width:100%;height:100%}
  .thumb--kitchen{left:10px}
  .thumb--kitchen div{background:linear-gradient(180deg,#d6d4cf 0%,#ecebe8 55%,#8a7a66 100%)}
  .thumb--bath{left:266px}
  .thumb--bath div{background:linear-gradient(90deg,#b9c2bf 0%,#d7ddd9 50%,#eeeeec 100%)}

  .description{position:absolute;left:50px;top:568px;width:440px;font-size:15.5px;line-height:19.7px;color:var(--ink)}

  .features{position:absolute;left:36px;top:709px;width:490px;height:261px;background:var(--panel-grey);padding:14px 16px}
  .features h3{font-size:17px;font-weight:700;color:var(--panel-head);line-height:20px}
  .features p{font-size:15px;line-height:20px;color:var(--panel-body);margin-bottom:10px}

  .price-panel{position:absolute;left:526px;top:283px;width:274px;height:425px;background:var(--black);color:var(--white)}
  .price{position:absolute;left:0;width:100%;top:22px;text-align:center;color:var(--red);font-size:56px;font-weight:700;letter-spacing:.5px}
  .specs{position:absolute;left:34px;top:112px;width:210px;border-collapse:collapse}
  .specs td{font-size:17px;height:29px;color:var(--white)}
  .specs td.value{font-weight:700;width:50px}
  .rule{position:absolute;left:33px;top:313px;width:208px;height:3px;background:var(--red)}
  .address{position:absolute;left:34px;top:342px;font-size:21px;line-height:27px}

  .agency-name{position:absolute;left:526px;top:760px;width:274px;text-align:center;font-weight:700;font-size:32px;line-height:30px;color:var(--black);letter-spacing:1px}
  .agency-name .mark{display:block;width:30px;height:30px;background:var(--red);margin:0 auto 14px}

  .brokerage{position:absolute;left:0;top:984px;width:317px;height:176px;background:var(--black);color:var(--white);padding:24px 24px 0}
  .brokerage-name{font-size:29px;font-weight:700;line-height:29px}
  .brokerage-sub{font-size:22px;line-height:26px;font-weight:700}
  .brokerage .rule-red{width:282px;height:3px;background:var(--red);margin:14px 0 16px -6px}
  .brokerage .notice{font-family:"Montserrat",Arial,sans-serif;font-size:18px;line-height:24px}
  .brokerage .notice strong{font-weight:600}

  .agent-band{position:absolute;left:317px;top:1007px;width:505px;height:127px;background:var(--red);color:var(--white)}
  .agent-name{position:absolute;left:25px;top:8px;font-size:42px;font-weight:700;white-space:nowrap}
  .agent-contact{position:absolute;left:32px;top:74px;font-size:19px;line-height:26px}
  .agent-contact span{display:flex;align-items:center;gap:8px}
  .agent-contact svg{width:14px;height:14px}
  .agent-photo{position:absolute;left:630px;top:945px;width:180px;height:215px;border-radius:90px 90px 0 0;
    background:linear-gradient(180deg,#c69a7f 0%,#a47c64 40%,#3a4049 62%,#1f2227 100%)}
</style>
</head>
<body>
<main class="flyer">
  <div class="hero-photo" role="img" aria-label="Exterior of a two-storey stucco condo building with exterior stairs and balcony railings in winter"></div>

  <div class="thumb thumb--kitchen"><div role="img" aria-label="Kitchen with white cabinets, range and refrigerator"></div></div>
  <div class="thumb thumb--bath"><div role="img" aria-label="Bathroom with glass shower door and toilet"></div></div>

  <p class="description">Just installed, new LVP flooring in living areas and hallway, new carpeting in bedrooms, complete interior paint and solid surface counters in kitchen. Bright and light end unit. Three bedrooms, two baths, two parking spots. Includes all appliances, washer/dryer in unit. Close to bases, shopping and dining. Dues include heat/hot water in addition to other expenses.</p>

  <section class="features">
    <h3>Dues Include</h3>
    <p>Exterior Maintenance, Grounds Maintenance, Heat, Insurance, Refuse, Sewer, Snow Removal, Water</p>
    <h3>Interior Features</h3>
    <p>CO Detector(s), Dishwasher, Disposal, Electric, Fireplace, Range/Oven, Refrigerator, Solid Surface Counter, Telephone, Washer &amp;/Or Dryer</p>
    <h3>Additional Features</h3>
    <p>Covenants/Restrictions, Deck/Patio, DSL/Cable Available, End unit, Fire Service Area, In City Limits, Pets Considered</p>
  </section>

  <aside class="price-panel">
    <div class="price">$111,000</div>
    <table class="specs">
      <tr><td>Beds</td><td class="value">3</td></tr>
      <tr><td>Baths</td><td class="value">2</td></tr>
      <tr><td>Garage / Carport</td><td class="value">0 / 0</td></tr>
      <tr><td>Square Ft.</td><td class="value">1267</td></tr>
      <tr><td>Lot Sq. Ft.</td><td class="value">0</td></tr>
      <tr><td>Acreage</td><td class="value">0</td></tr>
    </table>
    <div class="rule"></div>
    <div class="address">4820 N Birch Lane #B3<br>Ridgeview, AK 99000</div>
  </aside>

  <div class="agency-name"><span class="mark"></span>ELLERY<br>REALTY</div>

  <footer class="brokerage">
    <div class="brokerage-name">SUMMIT PEAK</div>
    <div class="brokerage-sub">REALTY NORTHLAND GROUP</div>
    <div class="rule-red"></div>
    <div class="notice"><strong>Each Office Independently</strong><br>Owned And Operated</div>
  </footer>

  <div class="agent-band">
    <div class="agent-name">Jordan Ellery</div>
    <div class="agent-contact">
      <span><svg viewBox="0 0 24 24" fill="none" stroke="#fff" stroke-width="2"><path d="M5 3h4l2 5-3 2a12 12 0 0 0 6 6l2-3 5 2v4a2 2 0 0 1-2 2A17 17 0 0 1 3 5a2 2 0 0 1 2-2z"/></svg>555-014-2290</span>
      <span><svg viewBox="0 0 24 24" fill="none" stroke="#fff" stroke-width="2"><rect x="2" y="5" width="20" height="14"/><path d="M2 5l10 8 10-8"/></svg>jellery@example.com</span>
    </div>
  </div>
  <div class="agent-photo" role="img" aria-label="Portrait of the agent in a dark blazer, arms crossed"></div>
</main>
</body>
</html>
```